Harnwick Aerial Services, LLC - Business Card

I currently have a drone business that specializes in aerial photography, thermal image inspections, deer recovery, search and rescue, custom agricultural applications. i will attach my current business card as well as some logos to incorporate for a new up to date business card
Updates

Designs look the same

Sick

Target Market(s)

farmers, hunters

Contact Information for Business Card

name address phone number (as existing card i attached)

Requirements
Must have
• im good with existing business card, but would like an agricultural twist

```html
<!DOCTYPE html>
<html lang="en">
<head>
<meta charset="utf-8">
<title>Harnwick Aerial Services, LLC - Business Card</title>
<link href="https://fonts.googleapis.com/css2?family=Arimo:wght@400;700&display=swap" rel="stylesheet">
<style>
  :root {
    --backdrop: #b1b2b1;
    --paper: #ffffff;
    --field-green: #4f9642;
    --ink: #060a0a;
    --on-green: #ffffff;
  }
  html, body {
    margin: 0;
    padding: 0;
    width: 1200px;
    height: 1200px;
    overflow: hidden;
    background: var(--backdrop);
    font-family: "Arimo", Arial, sans-serif;
  }
  .card {
    position: absolute;
    left: 279px;
    width: 642px;
    height: 366px;
    background: var(--paper);
    overflow: hidden;
  }
  .card--front { top: 196px; }
  .card--back { top: 638px; }
  .card__swoosh {
    position: absolute;
    inset: 0;
    width: 100%;
    height: 100%;
  }
  .swoosh-black { fill: var(--ink); }
  .swoosh-green { fill: var(--field-green); }

  .brand {
    position: absolute;
    display: flex;
    align-items: center;
    gap: 10px;
    color: var(--field-green);
    font-weight: 700;
  }
  .brand__dot {
    border-radius: 50%;
    background: var(--field-green);
  }
  .brand--front { left: 40px; top: 62px; font-size: 34px; }
  .brand--front .brand__dot { width: 30px; height: 30px; }
  .brand--back { left: 0; right: 0; top: 132px; justify-content: center; font-size: 46px; }
  .brand--back .brand__dot { width: 44px; height: 44px; }

  .owner {
    position: absolute;
    right: 39px;
    top: 46px;
    text-align: right;
  }
  .owner__name {
    margin: 0;
    font-size: 32px;
    font-weight: 700;
    color: var(--ink);
    line-height: 1.1;
  }
  .owner__title {
    margin: 0;
    font-size: 20px;
    font-weight: 700;
    color: var(--field-green);
    line-height: 1.2;
  }

  .services, .contact {
    position: absolute;
    top: 241px;
    margin: 0;
    padding: 0;
    list-style: none;
    color: var(--on-green);
    font-size: 17px;
    line-height: 26.4px;
  }
  .services { left: 31px; }
  .services li::before {
    content: "";
    display: inline-block;
    width: 10px;
    height: 2px;
    background: var(--on-green);
    vertical-align: middle;
    margin-right: 10px;
    position: relative;
    top: -3px;
  }
  .contact { right: 39px; text-align: right; }
</style>
</head>
<body>

<section class="card card--front" aria-label="Business card front">
  <svg class="card__swoosh" viewBox="0 0 802 458" preserveAspectRatio="none" aria-hidden="true">
    <path class="swoosh-black" d="M20 277 Q401 150 782 277 Q401 209 20 277 Z"/>
    <path class="swoosh-green" d="M0 297 Q401 207 802 297 L802 458 L0 458 Z"/>
  </svg>

  <div class="brand brand--front">
    <span class="brand__dot"></span>
    <span class="brand__name">Harnwick</span>
  </div>

  <div class="owner">
    <p class="owner__name">Dalton Mercer</p>
    <p class="owner__title">OWNER</p>
  </div>

  <ul class="services">
    <li>Thermal Image Inspections</li>
    <li>Deer Recovery</li>
    <li>Search &amp; Rescue</li>
    <li>Real Estate Photography</li>
  </ul>

  <ul class="contact">
    <li>555-014-2276</li>
    <li>www.harnwickaerial.com</li>
    <li>harnwickaerial@mail.com</li>
    <li>214 W. Elm St. Dalewood, OH 45000</li>
  </ul>
</section>

<section class="card card--back" aria-label="Business card back">
  <svg class="card__swoosh" viewBox="0 0 802 458" preserveAspectRatio="none" aria-hidden="true">
    <path class="swoosh-black" d="M20 410 Q401 280 782 410 Q401 340 20 410 Z"/>
    <path class="swoosh-green" d="M0 428 Q401 352 802 428 L802 458 L0 458 Z"/>
  </svg>

  <div class="brand brand--back">
    <span class="brand__dot"></span>
    <span class="brand__name">Harnwick</span>
  </div>
</section>

</body>
</html>
```